Flyer für Reinigungsdienstleister
Zielgruppe
Wir sind die Putzwerk Pilot und reinigen Privathaushalte. Wir fokussieren uns auf Reinigungen zu bezahlbaren Preisen, bei fairen Löhnen für Mitarbeiter. Nun suchen wir potentielle Kunden.
Aufgabenstellung
Für den Text liefern wir einen aktuellen Flyer, dieser enthält die wichtigsten Punkte.
Wir planen für 2025 eine große Kampagne mit Flyern zu begleiten und bräuchten dafür eine neue Version die wir auf die Kampagne anpassen.
Wir möchten 2 verschiedene Flyer erstellen, bei der Rückseite des bisherigen Flyers müsste keine großen Veränderung sein, lediglich die Vorderseite benötigt jeweils eine umfangreichere Anpassung.
1. Flyer:
Bei dem ersten Flyer geht es darum Kunden durch ein erstes kostenloses Probeputzen zu gewinnen.
Auf diesem sollte ein Bezug zum Angebot bestehen - gemäß dem Motto: Jetzt unverbindlich testen - wir schenken dir die erste Reinigung!
2. Flyer:
Bei dem 2. Flyer wollen wir einen Bezug zum Jahresstart. Dieser soll gemäß dem folgenden Motto angepasst werden:
Was ich mir für dieses Jahr vorgenommen habe? Mehr Freizeit - weniger Hausarbeit
Das geht ja auch ganz einfach, denn dafür gibt es die Putzwerk Pilot, die retten meine Freizeit!

```html
<!DOCTYPE html>
<html lang="de">
<head>
<meta charset="utf-8">
<title>Putzwerk Pilot – Flyer</title>
<link rel="stylesheet" href="https://fonts.googleapis.com/css2?family=Montserrat:wght@400;500;700;800&family=Oswald:wght@600&display=swap">
<style>
  :root {
    --bg: #e4f0f7;
    --ink: #475a86;
    --band: #526a93;
    --accent: #4fa8c7;
    --white: #ffffff;
  }
  * { margin: 0; padding: 0; box-sizing: border-box; }
  html, body { width: 849px; height: 1200px; overflow: hidden; }
  body { background: var(--bg); font-family: 'Montserrat', sans-serif; color: var(--ink); }
  .flyer { position: relative; width: 849px; height: 1200px; background: var(--bg); }
  .abs { position: absolute; }

  .hero-photo {
    left: 69px; top: 146px; width: 258px; height: 258px; border-radius: 50%;
    background: radial-gradient(circle at 70% 30%, #ffffff 0%, #eef2f5 35%, #e2b53a 55%, #22408a 80%, #1b2440 100%);
  }
  .brand-badge {
    left: 54px; top: 62px; width: 136px; height: 136px; border-radius: 50%;
    background: var(--white); border: 1.5px solid var(--ink);
    display: flex; align-items: center; justify-content: center; text-align: center;
  }
  .brand-name { font-weight: 700; font-size: 15px; line-height: 1.15; color: var(--ink); }

  .intro {
    left: 247px; top: 66px; width: 548px; font-size: 19px; line-height: 20.5px;
    letter-spacing: 0.9px; text-align: center;
  }

  .benefits { left: 383px; top: 208px; width: 440px; list-style: none; }
  .benefit { position: relative; padding-left: 28px; font-size: 16px; line-height: 23.5px; margin-bottom: 17px; }
  .benefit:nth-child(1) { line-height: 18px; margin-bottom: 26px; }
  .benefit::before {
    content: ""; position: absolute; left: 0; top: 4px; width: 17px; height: 17px;
    border-radius: 50%; background: var(--accent);
  }
  .benefit strong { font-weight: 800; }

  .services-band {
    left: 0; top: 503px; width: 849px; height: 63px; background: var(--band);
    display: flex; align-items: center; justify-content: center;
  }
  .services-title { font-family: 'Oswald', sans-serif; font-weight: 600; font-size: 38px; color: var(--white); letter-spacing: 0.5px; }

  .icon-disc {
    width: 84px; height: 84px; border-radius: 50%; background: var(--accent);
    display: flex; align-items: center; justify-content: center;
  }
  .icon-disc svg { width: 42px; height: 42px; fill: none; stroke: var(--white); stroke-width: 1.6; stroke-linecap: round; stroke-linejoin: round; }

  .service-photo {
    left: 343px; top: 749px; width: 248px; height: 248px; border-radius: 50%;
    background: radial-gradient(circle at 35% 25%, #ffffff 0%, #f2f2f2 35%, #c8a46e 60%, #8ea4bd 80%, #5a6b82 100%);
  }

  .service-title { font-weight: 700; font-size: 21px; white-space: nowrap; }
  .service-text { font-size: 16px; line-height: 18px; letter-spacing: 0.4px; }

  .contact-bar {
    left: 49px; top: 1113px; width: 761px; height: 49px; background: var(--band);
    color: var(--white); font-size: 16px; letter-spacing: 0.3px;
  }
  .contact-item { position: absolute; top: 0; height: 49px; display: flex; align-items: center; gap: 9px; }
  .contact-item svg { width: 19px; height: 19px; fill: none; stroke: var(--white); stroke-width: 1.5; stroke-linecap: round; stroke-linejoin: round; }
</style>
</head>
<body>
<main class="flyer">

  <div class="abs hero-photo" role="img" aria-label="Foto: Hand im gelben Gummihandschuh mit blauem Tuch und Sprühflasche"></div>
  <div class="abs brand-badge"><span class="brand-name">Putzwerk<br>Pilot</span></div>

  <p class="abs intro">Wir sind ein zuverlässiges und erfahrenes Reinigungs­unternehmen, das sich auf die Reinigung privater Haushalte spezialisiert hat. Lassen Sie uns die Arbeit erledigen, damit Sie die Ruhe eines sauberen und ordentlichen Zuhauses genießen können.</p>

  <ul class="abs benefits">
    <li class="benefit"><strong>Zuverlässigkeit:</strong> Professionelle und vertrauenswürdige Reinigungskräfte.</li>
    <li class="benefit"><strong>Flexibilität:</strong> Dienstleistungen, die<br>sich an Ihre Bedürfnisse anpassen.</li>
    <li class="benefit"><strong>Qualität:</strong> Hochwertige Reinigungs-<br>dienstleistungen.</li>
    <li class="benefit"><strong>Umweltfreundlich:</strong> Verwendung<br>umweltfreundlicher Reinigungsmittel.</li>
  </ul>

  <div class="abs services-band"><h2 class="services-title">UNSERE DIENSTLEISTUNGEN</h2></div>

  <div class="abs service-photo" role="img" aria-label="Foto: Reinigungskraft macht ein Bett, daneben ein Wäschekorb"></div>

  <div class="abs icon-disc" style="left:286px;top:611px">
    <svg viewBox="0 0 40 40"><path d="M12 10h12v4h-4l-2 4v3c4 2 5 5 5 9v5H11v-5c0-4 1-7 5-9v-3l-2-4"/><path d="M24 12l4 2"/><path d="M30 6l2-2M31 11h3M30 15l2 2"/></svg>
  </div>
  <div class="abs icon-disc" style="left:548px;top:611px">
    <svg viewBox="0 0 40 40"><path d="M20 9a2 2 0 1 1 2-2"/><path d="M20 9v2"/><path d="M11 13h18v3H11z"/><path d="M14 16l-2 6h4l-3 12h14l-3-12h4l-2-6"/></svg>
  </div>
  <div class="abs icon-disc" style="left:253px;top:885px">
    <svg viewBox="0 0 40 40"><circle cx="20" cy="20" r="15"/><circle cx="20" cy="20" r="10"/><path d="M12 9v22M17 10v5a2 2 0 0 1-4 0M24 9v22M27 10v22"/></svg>
  </div>
  <div class="abs icon-disc" style="left:600px;top:883px">
    <svg viewBox="0 0 40 40"><path d="M6 8h4l6 12"/><path d="M16 20h16l2 6H14z"/><path d="M20 20v-4h10v4"/><circle cx="16" cy="30" r="3"/><circle cx="30" cy="30" r="3"/></svg>
  </div>

  <h3 class="abs service-title" style="left:153px;top:713px">Tägliche Reinigung</h3>
  <p class="abs service-text" style="left:88px;top:746px;width:280px;text-align:center">Wohnzimmer, Küche, Badezimmer und Schlafzimmer, einschließlich schwer zugänglicher Bereiche.</p>

  <h3 class="abs service-title" style="left:537px;top:711px">Textilien</h3>
  <p class="abs service-text" style="left:548px;top:746px;width:270px;line-height:23.5px">Wäsche waschen, trocknen<br>&nbsp;&nbsp;&nbsp;&nbsp;&nbsp;&nbsp;und bügeln. Betten machen,<br>&nbsp;&nbsp;&nbsp;&nbsp;&nbsp;&nbsp;&nbsp;&nbsp;&nbsp;&nbsp;Bettwäschewechsel.</p>

  <h3 class="abs service-title" style="left:98px;top:983px">Einkauf &amp; Verpflegung</h3>
  <p class="abs service-text" style="left:96px;top:1015px;width:340px;line-height:24px">Einkaufen und Besorgungen erledigen.<br>Zubereitung von Mahlzeiten.</p>

  <h3 class="abs service-title" style="left:585px;top:975px">Gartenarbeit</h3>
  <p class="abs service-text" style="left:512px;top:1009px;width:222px;line-height:24px;text-align:right">Rasenmähen, Unkraut jäten und Pflanzenpflege.</p>

  <footer class="abs contact-bar">
    <div class="contact-item" style="left:27px">
      <svg viewBox="0 0 24 24"><path d="M5 3h4l2 5-3 2a12 12 0 0 0 6 6l2-3 5 2v4a2 2 0 0 1-2 2A17 17 0 0 1 3 5a2 2 0 0 1 2-2z"/></svg>
      <span>0152 000 12 345</span>
    </div>
    <div class="contact-item" style="left:239px">
      <svg viewBox="0 0 24 24"><rect x="2" y="5" width="20" height="14"/><path d="M2 5l10 8 10-8M2 19l7-7M22 19l-7-7"/></svg>
      <span>halle@putzwerkpilot.de</span>
    </div>
    <div class="contact-item" style="left:514px">
      <svg viewBox="0 0 24 24"><circle cx="12" cy="12" r="10"/><path d="M2 12h20M12 2c3 3 4 6 4 10s-1 7-4 10c-3-3-4-6-4-10s1-7 4-10z"/></svg>
      <span>www.putzwerkpilot.de</span>
    </div>
  </footer>

</main>
</body>
</html>
```